Bubble-Diagramm als Infografik für unseren Kunden aus der Immobilienbranche
Zielgruppe
Wir sind ein Software-Unternehmen mit Kunden aus allen Branchen. Ganz generell für unsere Homepage, konkret aber auch im Rahmen eines Kundenprojektes suchen wir ansprechende Beispiele und kreative Visualisierungen, wie Diagramme zu bestimmten Sachverhalten dargestellt werden können.
Aufgabenstellung
Wir möchten die Möglichkeiten darstellen, mit excelbasierten Diagrammtypen den gewissen „Wow-Effekt“ bei unseren Kunden hervorzurufen. Konkret geht es uns hier um die Erstellung eines Bubble-Diagramms. In einem Objektvergleich von Gewerbeimmobilien sollen drei Dimensionen (hier: Größe des Objekte, Gesamtmiete über die Laufzeit, effektive Miete je Quadratmeter) im Bubble-Diagramm dargestellt werden. Siehe hierzu Entwurf (.xls-Datei) anbei.
Eine Orientierung an unserem Firmenlayout (www.brenolux-net.de) ist ausdrücklich erwünscht. Die Grafik sollte aufgeräumt und klar wirken, ohne nüchtern zu sein, um auf der einen Seite mit der Form nicht vom Inhalt abzulenken, und sich auf der anderen Seite aber eben doch über die Form von der Konkurrenz, die nur mit Excel-Bordmitteln arbeitet, erkennbar abzuheben. Denkbar sind grundsätzlich auch Piktogramme oder vergleichbare, Inhalt transportierende Elemente im Graphik-Hintergrund oder in der Umrahmung, immer unter der Maßgabe, dass sie nicht zu verspielt daherkommen.
Technisch sind wir in der Lage, Excel-Diagramme auch „interaktiv“ zu gestalten, also nach Klick auf ein Diagrammelement ein Kontextmenü oder erweiterte Informationen einzublenden. Daher wünschen wir uns als Teil des Entwurfs, beispielhaft für eine Blase, die Darstellung so eines interaktiven Elements: eines Kontextmenüs / und oder eines Datenblatts.
Vorzugsweise soll die Grafik im Excel-Format zur Verfügung gestellt werden, das ist aber kein Must-have.

```html
<!DOCTYPE html>
<html lang="de">
<head>
<meta charset="utf-8">
<title>Bubble-Diagramm Objektvergleich</title>
<link rel="stylesheet" href="https://fonts.googleapis.com/css2?family=Questrial&family=Nunito:wght@700;800&display=swap">
<style>
  :root {
    --page-bg: #e9e9e9;
    --chart-bg: #323232;
    --backdrop-top: #3c3c3c;
    --backdrop-bottom: #4b4b4b;
    --band: #444444;
    --grid: #6a6a6a;
    --green: #8cc63f;
    --white: #ffffff;
    --bubble-inner: #f2f2f2;
    --text-light: #e6e6e6;
    --legend-text: #c8c8c8;
  }
  html, body {
    margin: 0;
    padding: 0;
    width: 900px;
    height: 1200px;
    overflow: hidden;
    background: var(--page-bg);
  }
  .canvas {
    position: relative;
    width: 900px;
    height: 1200px;
    display: flex;
    align-items: center;
    justify-content: center;
  }
  .bubble-chart {
    width: 860px;
    height: 484px;
    display: block;
  }
  .axis-value { font-family: "Nunito", sans-serif; font-weight: 800; fill: var(--text-light); font-size: 19px; }
  .axis-unit { font-family: "Nunito", sans-serif; font-weight: 700; font-size: 13px; fill: var(--text-light); }
  .axis-title { font-family: "Questrial", sans-serif; fill: var(--green); font-size: 30px; letter-spacing: 0.5px; }
  .legend-text { font-family: "Questrial", sans-serif; fill: var(--legend-text); font-size: 19px; letter-spacing: 0.4px; }
  .sheet-label, .sheet-value { font-family: "Nunito", sans-serif; font-weight: 800; fill: var(--green); font-size: 21px; }
</style>
</head>
<body>
<main class="canvas">
  <svg class="bubble-chart" viewBox="0 0 1457 820" xmlns="http://www.w3.org/2000/svg" aria-labelledby="chart-title">
    <title id="chart-title">Objektvergleich Gewerbeimmobilien: Effektivmiete je m² über Gesamtmiete, Blasengröße = Objektgröße</title>
    <defs>
      <linearGradient id="backdrop-fade" x1="0" y1="0" x2="0" y2="1">
        <stop offset="0" stop-color="var(--backdrop-top)"/>
        <stop offset="1" stop-color="var(--backdrop-bottom)"/>
      </linearGradient>
    </defs>

    <rect class="chart-bg" width="1457" height="820" fill="var(--chart-bg)"/>

    <!-- frame bands -->
    <g class="frame-bands" fill="var(--band)">
      <polygon points="46,0 84,0 84,57 46,82"/>
      <polygon points="46,380 84,355 84,820 46,820"/>
      <polygon points="0,749 503,749 525,787 0,787"/>
      <polygon points="722,749 1457,749 1457,787 744,787"/>
    </g>

    <!-- background illustration area -->
    <rect class="city-backdrop" role="img" aria-label="Illustration: Stadtsilhouette mit Bürohochhäusern und Wolke im Hintergrund"
      x="252" y="140" width="1032" height="513" fill="url(#backdrop-fade)"/>

    <!-- grid -->
    <g class="grid" stroke="var(--grid)" stroke-width="1.5">
      <line x1="153" y1="72" x2="248" y2="72"/>
      <line x1="153" y1="355" x2="1318" y2="355"/>
      <line x1="752" y1="123" x2="752" y2="720"/>
      <line x1="1284" y1="653" x2="1284" y2="720"/>
    </g>

    <!-- axes -->
    <g class="axes" stroke="var(--green)" stroke-width="5" stroke-linecap="round">
      <line x1="248" y1="72" x2="248" y2="717"/>
      <line x1="168" y1="653" x2="1284" y2="653"/>
    </g>

    <!-- trend line -->
    <line class="trend-line" x1="248" y1="653" x2="1311" y2="180" stroke="var(--green)" stroke-width="2"/>

    <!-- axis values -->
    <g class="y-values">
      <text class="axis-value" x="153" y="65">25€</text>
      <text class="axis-value" x="153" y="349">20€</text>
      <text class="axis-value" x="153" y="643">15€</text>
    </g>
    <g class="x-values">
      <text class="axis-value" x="258" y="718">5<tspan class="axis-unit">mio</tspan> €</text>
      <text class="axis-value" x="760" y="718">10<tspan class="axis-unit">mio</tspan> €</text>
      <text class="axis-value" x="1292" y="718">15<tspan class="axis-unit">mio</tspan> €</text>
    </g>

    <!-- axis titles -->
    <text class="axis-title" x="75" y="348" transform="rotate(-90 75 348)">Effektivmiete je m²</text>
    <text class="axis-title" x="623" y="777" text-anchor="middle">Gesamtmiete</text>

    <!-- legend -->
    <g class="legend">
      <circle cx="934" cy="65" r="18" fill="var(--white)" stroke="var(--green)" stroke-width="5"/>
      <text class="legend-text" x="964" y="71">Die Größe der Blasen zeigt die Objektgröße an.</text>
    </g>

    <!-- bubbles -->
    <g class="bubbles">
      <g class="bubble">
        <circle cx="548" cy="467" r="78" fill="var(--green)"/>
        <circle cx="548" cy="467" r="66" fill="var(--bubble-inner)" role="img" aria-label="Piktogramm Bürogebäude"/>
      </g>
      <g class="bubble">
        <circle cx="690" cy="412" r="65" fill="var(--green)"/>
        <circle cx="690" cy="412" r="54" fill="var(--bubble-inner)" role="img" aria-label="Piktogramm Bürogebäude"/>
      </g>
      <g class="bubble">
        <circle cx="802" cy="370" r="82" fill="var(--green)"/>
        <circle cx="802" cy="370" r="69" fill="var(--bubble-inner)" role="img" aria-label="Piktogramm Bürogebäude"/>
      </g>
      <g class="bubble">
        <circle cx="1015" cy="340" r="102" fill="var(--green)"/>
        <circle cx="1015" cy="340" r="87" fill="var(--bubble-inner)" role="img" aria-label="Piktogramm Bürogebäude"/>
      </g>
    </g>

    <!-- data sheet -->
    <g class="data-sheet">
      <polyline points="446,280 446,328 543,328 543,387" fill="none" stroke="var(--white)" stroke-width="2"/>
      <circle cx="446" cy="282" r="9" fill="var(--white)" stroke="#999" stroke-width="1.5"/>
      <circle cx="543" cy="387" r="9" fill="var(--white)"/>
      <rect x="310" y="145" width="283" height="135" fill="var(--white)"/>
      <path d="M310,167 V153 a8,8 0 0 1 8,-8 H585 a8,8 0 0 1 8,8 V167 Z" fill="var(--green)"/>
      <text class="sheet-label" x="326" y="198">Effektivmiete</text>
      <text class="sheet-value" x="496" y="198">20.30€</text>
      <text class="sheet-label" x="326" y="233">Gesamtmiete</text>
      <text class="sheet-value" x="496" y="233">8mio€</text>
      <text class="sheet-label" x="326" y="269">Größe</text>
      <text class="sheet-value" x="496" y="269">8000m<tspan font-size="10" dy="-9">2</tspan></text>
    </g>
  </svg>
</main>
</body>
</html>
```